innovative investment real estate sales firm

We are a uniquely collabrative firm that seeks to bring a conultative approach to uncovering hidden opportunities for our clients, our website needs to convey our client focused approach. Our firm specializes in the sale of apartment properties in Southern California. We have a team of researchers, transaction coordinators and marketing personal to support our geographically specialized advisers. We need a website that introduces clients to our unique way of better helping them achieve their investment goals.

Target Market(s)

High net worth individuals and families

Industry/Entity Type

Real Estate Agent

Font styles to use
Other font styles liked:
• please use font provided

Requirements
Must have
• Stories of our recent projects
• Features on our people
• email capture for viewing inventory
• content that showcases our unique consultative approach that uncovers unrealized opportunities

```html
<!DOCTYPE html>
<html lang="en">
<head>
<meta charset="utf-8">
<title>Meridian Crest Advisers</title>
<link rel="stylesheet" href="https://fonts.googleapis.com/css2?family=Montserrat:wght@400;500;600;700&family=Open+Sans:wght@400;600;700&family=Libre+Baskerville&display=swap">
<style>
:root{
  --teal:#1ba4b6;
  --teal-dark:#148a9a;
  --green:#8cc63f;
  --ink:#222a33;
  --text:#555b62;
  --muted:#8a9097;
  --line:#e1e4e7;
  --soft:#f4f5f6;
  --white:#ffffff;
  --dark:#2c3540;
}
*{box-sizing:border-box;margin:0;padding:0}
html,body{width:1200px;height:3982px;overflow:hidden}
body{font-family:"Open Sans",Arial,sans-serif;color:var(--text);background:var(--white);font-size:13px}
h1,h2,h3,h4{font-family:"Montserrat",Arial,sans-serif;color:var(--ink)}
.svg-icon{display:block}

/* header */
.site-header{height:95px;display:flex;align-items:center;padding:0 88px 0 85px;background:var(--white)}
.brand{display:flex;align-items:center;gap:10px;width:260px}
.brand-mark{width:30px;height:30px;border:3px solid var(--teal)}
.brand-name{font-family:"Montserrat",sans-serif;font-weight:700;font-size:17px;color:var(--teal-dark);letter-spacing:.5px;line-height:1.1}
.main-nav{display:flex;gap:26px;margin-left:auto;margin-right:28px}
.main-nav a{font-family:"Montserrat",sans-serif;font-size:12.5px;color:var(--ink);text-decoration:none;padding:6px 0}
.main-nav a.active{color:var(--green);border-bottom:2px solid var(--green)}
.phone-btn{background:var(--teal);color:var(--white);font-family:"Montserrat",sans-serif;font-weight:600;font-size:13px;height:40px;padding:0 16px;display:flex;align-items:center;gap:12px}

/* hero */
.hero{height:503px;position:relative;background:linear-gradient(180deg,#2a8fa0 0%,#1f7d8e 50%,#2a4d5e 100%);text-align:center;color:var(--white)}
.hero-title{padding-top:145px;color:var(--white);font-size:30px;font-weight:600;line-height:1.5}
.hero-text{margin:10px auto 0;width:470px;font-size:13px;line-height:1.6;opacity:.9}
.hero-down{width:38px;height:38px;border:1px solid rgba(255,255,255,.6);margin:36px auto 0;display:flex;align-items:center;justify-content:center}

/* section titles */
.section-title{text-align:center;font-size:22px;font-weight:600;text-transform:uppercase}
.section-title::after{content:"";display:block;width:40px;height:2px;background:var(--green);margin:14px auto 0}

/* properties */
.properties{height:717px;background:var(--soft);padding-top:90px}
.property-grid{display:flex;gap:28px;margin:44px 85px 0}
.property-card{width:237px;background:var(--white);border:1px solid var(--line)}
.property-photo{height:212px;position:relative;background:linear-gradient(135deg,#d9dde0,#b8bec3 60%,#8f969c)}
.price-tag{position:absolute;right:0;bottom:0;background:var(--green);color:var(--white);font-weight:700;font-size:14px;padding:7px 12px}
.property-info{padding:14px 12px 10px}
.property-name{font-size:13px;font-weight:700;color:var(--ink);font-family:"Open Sans",sans-serif}
.property-address{display:flex;align-items:center;gap:5px;font-size:10.5px;color:var(--muted);margin-top:6px}
.property-meta{display:flex;border-top:1px solid var(--line)}
.property-meta span{flex:1;display:flex;align-items:center;justify-content:center;gap:8px;height:42px;font-size:11px;color:var(--text);border-right:1px solid var(--line)}
.property-meta span:last-child{border-right:none}
.btn-green{display:flex;align-items:center;gap:14px;margin:66px auto 0;width:213px;height:62px;background:var(--green);color:var(--white);font-family:"Montserrat",sans-serif;font-size:11px;font-weight:700;justify-content:center;text-transform:uppercase}

/* stats */
.stats{height:293px;background:linear-gradient(180deg,#39434f,#262e38);display:flex;justify-content:center;gap:74px;padding-top:75px}
.stat{width:190px;height:150px;background:rgba(255,255,255,.07);border:1px solid rgba(255,255,255,.1);text-align:center;color:var(--white);padding-top:40px}
.stat-num{font-family:"Montserrat",sans-serif;font-size:36px;font-weight:500}
.stat-label{font-size:11px;font-weight:700;text-transform:uppercase;margin-top:8px;letter-spacing:.5px}

/* about */
.about{height:644px;display:flex}
.about-text{width:607px;background:var(--soft);padding:62px 50px 0 85px}
.about-text h2{font-size:22px;font-weight:500}
.about-intro{margin-top:18px;font-size:12px;line-height:1.6;width:470px}
.features{display:grid;grid-template-columns:275px 200px;row-gap:38px;margin-top:36px}
.feature-icon{width:96px;height:96px;border-radius:50%;border:2px solid #4a4f55;display:flex;align-items:center;justify-content:center;background:var(--white)}
.feature-icon.active{border-color:var(--teal)}
.feature h3{font-family:"Open Sans",sans-serif;font-size:12.5px;font-weight:600;margin-top:20px}
.feature.active h3{color:var(--teal)}
.feature p{font-size:11.5px;line-height:1.55;margin-top:6px;width:180px}
.about-photo{flex:1;background:linear-gradient(160deg,#e9ecee 0%,#c9cfd3 45%,#b7875a 80%,#a87545 100%)}

/* agents */
.agents{height:663px;padding-top:88px;position:relative}
.agent-row{display:flex;gap:64px;margin:52px 0 0 140px}
.agent{width:180px;text-align:center}
.agent-photo{height:282px;background:linear-gradient(180deg,#eceeef,#c4c8cc 70%,#2e3238);border:1px solid var(--line)}
.agent-name{font-family:"Open Sans",sans-serif;font-size:11px;font-weight:600;color:var(--ink);margin-top:18px}
.agent-role{font-size:10px;color:var(--muted);margin-top:4px}
.agent-social{display:flex;gap:6px;justify-content:center;margin-top:12px}
.agent-social i{width:26px;height:26px;background:#3a4048;display:block}
.carousel-arrow{position:absolute;top:2582px;width:42px;height:42px;border:2px solid var(--teal);border-radius:50%;display:flex;align-items:center;justify-content:center;background:var(--white)}

/* testimonial */
.testimonial{height:495px;position:relative;background:linear-gradient(180deg,#1ba4b6,#178fa0);color:var(--white);text-align:center;padding-top:100px}
.reviewer{display:flex;align-items:center;justify-content:center;gap:14px;margin-left:120px}
.reviewer-photo{width:96px;height:96px;border-radius:50%;border:4px solid var(--white);background:linear-gradient(160deg,#e7c6b5,#8b5a4a)}
.reviewer-name{font-size:11px;font-weight:700;text-align:left;text-transform:uppercase}
.reviewer-role{font-size:10px;text-align:left;opacity:.85}
.quote{width:700px;margin:28px auto 0;font-size:12px;line-height:1.75;position:relative}
.quote b{font-family:"Libre Baskerville",serif;font-size:34px;position:absolute;top:-10px}
.slider-dots{display:flex;gap:8px;justify-content:center;margin-top:24px}
.slider-dots i{width:26px;height:2px;background:rgba(255,255,255,.45);display:block}
.slider-dots i.on{background:var(--white)}
.signup{position:absolute;left:330px;top:417px;width:535px;height:155px;background:var(--white);display:flex;box-shadow:0 4px 16px rgba(0,0,0,.12);text-align:left}
.signup-photo{width:130px;background:linear-gradient(180deg,#cfe3ea,#8fa8b3)}
.signup-body{flex:1;padding:18px 20px;color:var(--text)}
.signup-body h3{font-family:"Libre Baskerville",serif;font-weight:400;font-size:18px;color:var(--ink)}
.signup-body p{font-size:10.5px;line-height:1.5;margin-top:6px}
.signup-field{margin-top:12px;height:34px;width:300px;border:1px solid #bfc4c9;font-size:10px;color:var(--muted);padding:10px}
.signup-go{width:52px;background:var(--green);display:flex;align-items:center;justify-content:center}

/* footer */
.site-footer{height:480px;padding:170px 85px 0;display:flex;position:relative}
.footer-col h4{font-size:12px;font-weight:600;text-transform:uppercase}
.footer-col h4::after{content:"";display:block;width:24px;height:2px;background:var(--green);margin-top:8px}
.col-landmark{width:308px}
.col-links{width:194px}
.col-news{width:297px}
.col-property{width:230px}
.footer-col p,.footer-col li{font-size:10.5px;line-height:1.7}
.footer-col ul{list-style:none;margin-top:18px}
.footer-col li{line-height:2.25}
.landmark-text{margin-top:18px;width:210px}
.contact-line{display:flex;align-items:center;gap:10px;margin-top:12px;font-size:10.5px}
.contact-dot{width:24px;height:24px;border-radius:50%;background:#33393f;display:flex;align-items:center;justify-content:center;flex:none}
.news-card{margin-top:20px;width:212px;height:196px;background:linear-gradient(180deg,#d9dcdf,#9aa0a6);position:relative}
.news-card span{position:absolute;left:10px;top:10px;width:130px;background:rgba(34,42,51,.82);color:var(--white);font-size:9.5px;font-weight:700;padding:6px;line-height:1.35}
.mini-property{display:flex;gap:12px;margin-top:18px}
.mini-photo{width:60px;height:46px;background:linear-gradient(135deg,#e0d6cc,#a89482);flex:none}
.mini-property p{font-size:10px;line-height:1.45}
.mini-property b{color:var(--ink);font-size:10.5px}
.bottom-bar{height:92px;border-top:1px solid var(--line);margin:0 85px;display:flex;align-items:center;justify-content:space-between;font-size:10.5px}
.bottom-bar strong{color:var(--teal);font-weight:600}
.social-circles{display:flex;gap:10px}
.social-circles i{width:34px;height:34px;border:2px solid var(--teal);border-radius:50%;display:block}
</style>
</head>
<body>

<header class="site-header">
  <div class="brand"><span class="brand-mark"></span><span class="brand-name">MERIDIAN CREST<br>ADVISERS</span></div>
  <nav class="main-nav">
    <a class="active">Home</a><a>About Us</a><a>Services</a><a>Properties</a><a>Recent projects</a><a>Our Team</a><a>News</a><a>Contact</a>
  </nav>
  <div class="phone-btn">
    <svg class="svg-icon" width="14" height="14" viewBox="0 0 24 24"><path fill="#fff" d="M6.6 10.8a15 15 0 006.6 6.6l2.2-2.2c.3-.3.7-.4 1-.2 1.1.4 2.3.6 3.6.6.6 0 1 .4 1 1V20c0 .6-.4 1-1 1A17 17 0 013 4c0-.6.4-1 1-1h3.5c.6 0 1 .4 1 1 0 1.3.2 2.5.6 3.6.1.3 0 .7-.2 1z"/></svg>
    (555) 010-4580
  </div>
</header>

<section class="hero" role="img" aria-label="City skyline of high-rise apartment towers at dusk under a teal overlay">
  <h1 class="hero-title">Feel the Luxury, Royalness and Comfort with<br>Meridian Crest Advisers</h1>
  <p class="hero-text">Aliquam velit commodo sit amet vestibulum hendrerit lucen Donec facilisis sapien erat in fauc dui vehicula.</p>
  <div class="hero-down"><svg class="svg-icon" width="16" height="16" viewBox="0 0 16 16"><path d="M3 5l5 6 5-6" fill="none" stroke="#fff" stroke-width="1.5"/></svg></div>
</section>

<section class="properties">
  <h2 class="section-title">Recent Properties</h2>
  <div class="property-grid">
    <article class="property-card">
      <div class="property-photo" role="img" aria-label="Bright modern living room interior"><span class="price-tag">$ 430.00</span></div>
      <div class="property-info"><h3 class="property-name">Pellentesque Convallis</h3><p class="property-address"><svg width="9" height="11" viewBox="0 0 12 16"><path d="M6 0a6 6 0 00-6 6c0 4.5 6 10 6 10s6-5.5 6-10a6 6 0 00-6-6zm0 8.5A2.5 2.5 0 116 3.5a2.5 2.5 0 010 5z" fill="#e5a12a"/></svg>48 Harbor Lane California</p></div>
      <div class="property-meta"><span><svg width="16" height="11" viewBox="0 0 16 11"><path d="M1 0v11M1 7h14v4M4 4h10v3" fill="none" stroke="#666" stroke-width="1.3"/></svg>3</span><span><svg width="13" height="13" viewBox="0 0 13 13"><rect x=".7" y=".7" width="11.6" height="11.6" fill="none" stroke="#666" stroke-width="1.3"/><path d="M.7 6.5h6v5.8" fill="none" stroke="#666" stroke-width="1.3"/></svg>2630</span><span><svg width="16" height="12" viewBox="0 0 16 12"><path d="M1 5h14v2a4 4 0 01-4 4H5a4 4 0 01-4-4zM3 5V1h3" fill="none" stroke="#666" stroke-width="1.3"/></svg>2</span></div>
    </article>
    <article class="property-card">
      <div class="property-photo" role="img" aria-label="Sunlit apartment living area with tall windows"><span class="price-tag">$ 430.00</span></div>
      <div class="property-info"><h3 class="property-name">Pellentesque Convallis</h3><p class="property-address"><svg width="9" height="11" viewBox="0 0 12 16"><path d="M6 0a6 6 0 00-6 6c0 4.5 6 10 6 10s6-5.5 6-10a6 6 0 00-6-6zm0 8.5A2.5 2.5 0 116 3.5a2.5 2.5 0 010 5z" fill="#e5a12a"/></svg>48 Harbor Lane California</p></div>
      <div class="property-meta"><span><svg width="16" height="11" viewBox="0 0 16 11"><path d="M1 0v11M1 7h14v4M4 4h10v3" fill="none" stroke="#666" stroke-width="1.3"/></svg>3</span><span><svg width="13" height="13" viewBox="0 0 13 13"><rect x=".7" y=".7" width="11.6" height="11.6" fill="none" stroke="#666" stroke-width="1.3"/><path d="M.7 6.5h6v5.8" fill="none" stroke="#666" stroke-width="1.3"/></svg>2630</span><span><svg width="16" height="12" viewBox="0 0 16 12"><path d="M1 5h14v2a4 4 0 01-4 4H5a4 4 0 01-4-4zM3 5V1h3" fill="none" stroke="#666" stroke-width="1.3"/></svg>2</span></div>
    </article>
    <article class="property-card">
      <div class="property-photo" role="img" aria-label="Warm open-plan dining and kitchen interior" style="background:linear-gradient(135deg,#e8d9c6,#c9a27c 60%,#8f6a4a)"><span class="price-tag">$ 430.00</span></div>
      <div class="property-info"><h3 class="property-name">Pellentesque Convallis</h3><p class="property-address"><svg width="9" height="11" viewBox="0 0 12 16"><path d="M6 0a6 6 0 00-6 6c0 4.5 6 10 6 10s6-5.5 6-10a6 6 0 00-6-6zm0 8.5A2.5 2.5 0 116 3.5a2.5 2.5 0 010 5z" fill="#e5a12a"/></svg>48 Harbor Lane California</p></div>
      <div class="property-meta"><span><svg width="16" height="11" viewBox="0 0 16 11"><path d="M1 0v11M1 7h14v4M4 4h10v3" fill="none" stroke="#666" stroke-width="1.3"/></svg>3</span><span><svg width="13" height="13" viewBox="0 0 13 13"><rect x=".7" y=".7" width="11.6" height="11.6" fill="none" stroke="#666" stroke-width="1.3"/><path d="M.7 6.5h6v5.8" fill="none" stroke="#666" stroke-width="1.3"/></svg>2630</span><span><svg width="16" height="12" viewBox="0 0 16 12"><path d="M1 5h14v2a4 4 0 01-4 4H5a4 4 0 01-4-4zM3 5V1h3" fill="none" stroke="#666" stroke-width="1.3"/></svg>2</span></div>
    </article>
    <article class="property-card">
      <div class="property-photo" role="img" aria-label="Modern living room with grey sofa and window"><span class="price-tag">$ 430.00</span></div>
      <div class="property-info"><h3 class="property-name">Pellentesque Convallis</h3><p class="property-address"><svg width="9" height="11" viewBox="0 0 12 16"><path d="M6 0a6 6 0 00-6 6c0 4.5 6 10 6 10s6-5.5 6-10a6 6 0 00-6-6zm0 8.5A2.5 2.5 0 116 3.5a2.5 2.5 0 010 5z" fill="#e5a12a"/></svg>48 Harbor Lane California</p></div>
      <div class="property-meta"><span><svg width="16" height="11" viewBox="0 0 16 11"><path d="M1 0v11M1 7h14v4M4 4h10v3" fill="none" stroke="#666" stroke-width="1.3"/></svg>3</span><span><svg width="13" height="13" viewBox="0 0 13 13"><rect x=".7" y=".7" width="11.6" height="11.6" fill="none" stroke="#666" stroke-width="1.3"/><path d="M.7 6.5h6v5.8" fill="none" stroke="#666" stroke-width="1.3"/></svg>2630</span><span><svg width="16" height="12" viewBox="0 0 16 12"><path d="M1 5h14v2a4 4 0 01-4 4H5a4 4 0 01-4-4zM3 5V1h3" fill="none" stroke="#666" stroke-width="1.3"/></svg>2</span></div>
    </article>
  </div>
  <div class="btn-green"><svg width="26" height="26" viewBox="0 0 26 26"><path d="M3 23V8h8v15M11 23V3h12v20M2 23h22M15 8h4M15 13h4M15 18h4M6 12h2M6 17h2" fill="none" stroke="#fff" stroke-width="1.4"/></svg>View our properties</div>
</section>

<section class="stats" role="img" aria-label="Dark city skyline behind key figures">
  <div class="stat"><div class="stat-num">812</div><div class="stat-label">Properties</div></div>
  <div class="stat"><div class="stat-num">25</div><div class="stat-label">Agents</div></div>
  <div class="stat"><div class="stat-num">485</div><div class="stat-label">Contracted</div></div>
  <div class="stat"><div class="stat-num">380</div><div class="stat-label">Happy Clients</div></div>
</section>

<section class="about">
  <div class="about-text">
    <h2>About Meridian Crest Advisers</h2>
    <p class="about-intro">We are a uniquely collaborative firm that seeks to bring a consultative approach to uncovering hidden opportunities for our clients, our website needs to convey our client focused approach.</p>
    <div class="features">
      <div class="feature active">
        <div class="feature-icon active"><svg width="44" height="44" viewBox="0 0 44 44"><path d="M6 21L22 7l16 14" fill="none" stroke="#1ba4b6" stroke-width="3"/><path d="M11 18v19h22V18" fill="#1ba4b6"/><rect x="18" y="26" width="8" height="11" fill="#fff"/></svg></div>
        <h3>Unique Consultative Firm</h3><p>Ipurus, posuere feugiat elit vel, fermentum vehicula ex.</p>
      </div>
      <div class="feature">
        <div class="feature-icon"><svg width="46" height="46" viewBox="0 0 46 46"><g stroke="#3a4048" stroke-width="1.6" fill="none"><circle cx="23" cy="23" r="5"/><circle cx="23" cy="6" r="3"/><circle cx="23" cy="40" r="3"/><circle cx="6" cy="23" r="3"/><circle cx="40" cy="23" r="3"/><circle cx="10" cy="10" r="3"/><circle cx="36" cy="36" r="3"/><path d="M23 9v9M23 28v9M9 23h9M28 23h9M12 12l7 7M27 27l7 7"/></g></svg></div>
        <h3>Consultative Approach</h3><p>Ipurus, posuere feugiat elit vel, fermentum vehicula ex.</p>
      </div>
      <div class="feature">
        <div class="feature-icon"><svg width="40" height="40" viewBox="0 0 40 40"><path d="M4 18h7v18H4zM11 19l8-14c3 0 4 2 3 6l-1 5h11c2 0 3 2 2.5 4L32 33c-.5 2-2 3-4 3H11" fill="none" stroke="#3a4048" stroke-width="1.8" stroke-linejoin="round"/></svg></div>
        <h3>Premium Quality</h3><p>Ipurus, posuere feugiat elit vel, fermentum vehicula ex.</p>
      </div>
      <div class="feature">
        <div class="feature-icon"><svg width="42" height="42" viewBox="0 0 42 42"><g fill="none" stroke="#3a4048" stroke-width="1.7"><circle cx="21" cy="11" r="5"/><path d="M13 23c0-4 4-6 8-6s8 2 8 6"/><path d="M4 24l7 8h8M38 24l-7 8h-8M11 32v6M31 32v6"/></g></svg></div>
        <h3>Friendly Customer Support</h3><p>Ipurus, posuere feugiat elit vel, fermentum vehicula ex.</p>
      </div>
    </div>
  </div>
  <div class="about-photo" role="img" aria-label="Advisers showing a couple around a bright loft with large windows and wooden floor"></div>
</section>

<section class="agents">
  <h2 class="section-title">Meet Our Agents</h2>
  <div class="agent-row">
    <div class="agent"><div class="agent-photo" role="img" aria-label="Portrait of agent in dark suit"></div><p class="agent-name">LISA RESOURC</p><p class="agent-role">Nullam ameacurus ipsum</p><div class="agent-social"><i></i><i></i><i></i></div></div>
    <div class="agent"><div class="agent-photo" role="img" aria-label="Portrait of agent in dark suit"></div><p class="agent-name">LISA RESOURC</p><p class="agent-role">Nullam ameacurus ipsum</p></div>
    <div class="agent"><div class="agent-photo" role="img" aria-label="Portrait of agent in dark suit"></div><p class="agent-name">LISA RESOURC</p><p class="agent-role">Nullam ameacurus ipsum</p></div>
    <div class="agent"><div class="agent-photo" role="img" aria-label="Portrait of agent in dark suit"></div><p class="agent-name">LISA RESOURC</p><p class="agent-role">Nullam ameacurus ipsum</p></div>
  </div>
  <div class="carousel-arrow" style="left:84px;top:330px"><svg width="12" height="12" viewBox="0 0 12 12"><path d="M8 1L3 6l5 5" fill="none" stroke="#1ba4b6" stroke-width="2"/></svg></div>
  <div class="carousel-arrow" style="left:1070px;top:330px"><svg width="12" height="12" viewBox="0 0 12 12"><path d="M4 1l5 5-5 5" fill="none" stroke="#1ba4b6" stroke-width="2"/></svg></div>
</section>

<section class="testimonial" role="img" aria-label="City skyline under a teal overlay behind a client testimonial">
  <div class="reviewer">
    <div class="reviewer-photo" role="img" aria-label="Client portrait"></div>
    <div><p class="reviewer-name">Aliksmod Congueqert</p><p class="reviewer-role">House wife</p></div>
  </div>
  <p class="quote"><b style="left:-30px">&ldquo;</b>Curabitur imperdiet quis purus et sodales. Proin purus libero, bibendum nec maximus eu, ullamcorper sed lacus. Aliquam in est pretium, varius tortor at, molestie lectus. Aliquam velit ex, commodo sit amet vestibulum in, hendrerit eu orci<b style="right:-30px">&rdquo;</b></p>
  <div class="slider-dots"><i class="on"></i><i></i><i></i><i></i></div>

  <div class="signup">
    <div class="signup-photo" role="img" aria-label="Apartment tower exterior"></div>
    <div class="signup-body">
      <h3>Email Signup for viewing inventory</h3>
      <p>Curabitur imperdiet quis purus et sodales. Proin purus libero, bibendum nec maximus.</p>
      <div class="signup-field">Email Address</div>
    </div>
    <div class="signup-go"><svg width="12" height="18" viewBox="0 0 12 18"><path d="M2 2l7 7-7 7" fill="none" stroke="#fff" stroke-width="2.5"/></svg></div>
  </div>
</section>

<footer class="site-footer">
  <div class="footer-col col-landmark">
    <h4>Landmark</h4>
    <p class="landmark-text">Etiam hendrerit metus augue, mollis sagittis neque auctor quis Aenean finibus ante et lectus convallis</p>
    <div class="contact-line"><span class="contact-dot"><svg width="10" height="12" viewBox="0 0 12 16"><path d="M6 0a6 6 0 00-6 6c0 4.5 6 10 6 10s6-5.5 6-10a6 6 0 00-6-6z" fill="#fff"/></svg></span>48 Harbor Lane, Suite 12<br>sodales Proin purus</div>
    <div class="contact-line"><span class="contact-dot"><svg width="10" height="10" viewBox="0 0 24 24"><path fill="#fff" d="M6.6 10.8a15 15 0 006.6 6.6l2.2-2.2c.3-.3.7-.4 1-.2 1.1.4 2.3.6 3.6.6.6 0 1 .4 1 1V20c0 .6-.4 1-1 1A17 17 0 013 4c0-.6.4-1 1-1h3.5c.6 0 1 .4 1 1 0 1.3.2 2.5.6 3.6.1.3 0 .7-.2 1z"/></svg></span>(555) 010-4580</div>
    <div class="contact-line"><span class="contact-dot"><svg width="11" height="8" viewBox="0 0 22 16"><rect x="1" y="1" width="20" height="14" fill="none" stroke="#fff" stroke-width="2"/><path d="M1 1l10 8 10-8" fill="none" stroke="#fff" stroke-width="2"/></svg></span>hello@meridiancrest.example</div>
  </div>
  <div class="footer-col col-links">
    <h4>Useful Links</h4>
    <ul><li>Home</li><li>About Us</li><li>Services</li><li>Properties</li><li>Recent projects</li><li>Our Team</li><li>News</li><li>Contact</li></ul>
  </div>
  <div class="footer-col col-news">
    <h4>Latest News</h4>
    <div class="news-card" role="img" aria-label="Interior of a furnished apartment"><span>ETIAM HENDRERIT METUS AUGUE, MOLLIS SAGITTIS NEQUE<br>25.01.17</span></div>
  </div>
  <div class="footer-col col-property">
    <h4>Latest Property</h4>
    <div class="mini-property"><div class="mini-photo" role="img" aria-label="Apartment interior"></div><p>Etiam hendrerit metus augue, mollis sagittisconvallis<br><b>$ 430.00</b></p></div>
    <div class="mini-property"><div class="mini-photo" role="img" aria-label="Apartment interior"></div><p>Etiam hendrerit metus augue, mollis sagittisconvallis<br><b>$ 430.00</b></p></div>
    <div class="mini-property"><div class="mini-photo" role="img" aria-label="Apartment interior"></div><p>Etiam hendrerit metus augue, mollis sagittisconvallis<br><b>$ 430.00</b></p></div>
  </div>
</footer>
<div class="bottom-bar">
  <p>© 2017 <strong>Meridian Crest Advisers</strong> . All Rights Reserved</p>
  <div class="social-circles"><i></i><i></i><i></i></div>
</div>

</body>
</html>
```